Printable PDF Template for "Do it yourself" receipts needed

We need a reusable Template for PDF. Content is Do it yourself related.
Elements should be easy to exchange.

Here you can find some samples:
http://www.wundertagsfreude.de/downloads/bastelkiste/aus_muesliverpackung_wird_notizheft.pdf
http://www.wundertagsfreude.de/downloads/bastelkiste/teelichthalter_aus_plastikflasche.pdf
http://www.wundertagsfreude.de/downloads/bastelkiste/lampe_aus_getraenkekartons.pdf

Font styles to use
Decorative

```html
<!DOCTYPE html>
<html lang="en">
<head>
<meta charset="utf-8">
<title>DIY Guide – Template</title>
<link rel="stylesheet" href="https://fonts.googleapis.com/css2?family=Questrial&family=Kalam:wght@700&display=swap">
<style>
  :root {
    --paper: #f7f1de;
    --panel: #ffffff;
    --frame-green: #8cc63f;
    --dot-pink: #f7b3c6;
    --number-orange: #f58a2e;
    --ink: #4a4a4a;
    --heading-ink: #555555;
    --petal-pink: #f6a9bf;
    --petal-rose: #e983b4;
    --bloom-orange: #f59332;
    --bloom-mint: #a9dccd;
    --bloom-yellow: #f9dc6b;
    --bloom-olive: #a7b45a;
  }
  * { box-sizing: border-box; margin: 0; padding: 0; }
  html, body { width: 848px; height: 1200px; overflow: hidden; }
  body {
    position: relative;
    background: var(--paper);
    font-family: "Questrial", "Century Gothic", sans-serif;
    color: var(--ink);
  }
  .bloom-side {
    position: absolute; left: 0; top: 390px; width: 110px; height: 810px;
    background: linear-gradient(180deg, var(--bloom-mint) 0%, var(--petal-pink) 22%, var(--bloom-yellow) 45%, var(--bloom-orange) 62%, var(--bloom-olive) 88%);
    border-top-right-radius: 60px;
    opacity: .85;
  }
  .bloom-bottom {
    position: absolute; left: 0; bottom: 0; width: 848px; height: 110px;
    background: linear-gradient(90deg, var(--bloom-olive) 0%, var(--bloom-orange) 25%, var(--bloom-mint) 45%, var(--bloom-yellow) 65%, var(--petal-pink) 90%);
    opacity: .85;
  }
  .page {
    position: absolute; left: 63px; top: 68px; width: 718px; height: 1041px;
    background: var(--panel);
  }
  .frame {
    position: absolute; left: 78px; top: 86px; width: 689px; height: 1011px;
    border: 1.5px dashed var(--frame-green);
  }
  .image-slot {
    position: absolute; width: 328px; height: 328px; border-radius: 50%;
    background: var(--panel);
    border: 1.5px dashed var(--frame-green);
    display: flex; align-items: center; justify-content: center;
    font-size: 24px; letter-spacing: .5px; color: var(--heading-ink);
  }
  .image-slot--first { left: 33px; top: 102px; }
  .image-slot--second { left: 472px; top: 715px; }
  .step { position: absolute; }
  .step__head { display: flex; align-items: flex-start; }
  .step__number {
    font-family: "Kalam", cursive; font-weight: 700; color: var(--number-orange);
    font-size: 66px; line-height: 1; margin-right: 6px; margin-top: 2px;
  }
  .step__title { font-size: 24px; line-height: 30px; color: var(--heading-ink); margin-top: -2px; }
  .step__body { font-size: 18.5px; line-height: 23.6px; color: var(--ink); margin-top: 30px; }
  .step__body p + p { margin-top: 23.6px; }
  .step--first { left: 385px; top: 118px; }
  .step--second { left: 105px; top: 557px; }
  .step--second .step__body { margin-top: 36px; }
  .divider { position: absolute; left: 133px; top: 505px; }
  .petal { position: absolute; }
  .petal--upper { left: 640px; top: 590px; }
  .petal--lower { left: 336px; top: 938px; }
</style>
</head>
<body>
  <div class="bloom-side" role="img" aria-label="Illustrated pastel flower bursts along the left edge"></div>
  <div class="bloom-bottom" role="img" aria-label="Illustrated pastel flower bursts along the bottom edge"></div>

  <main class="page"></main>
  <div class="frame"></div>

  <div class="image-slot image-slot--first">IMAGE 1</div>

  <section class="step step--first">
    <div class="step__head">
      <span class="step__number">1</span>
      <h2 class="step__title">Title<br>Title Second Line</h2>
    </div>
    <div class="step__body">
      <p>Lorem Ipsum is simply dummy text of<br>the printing and typesetting industry.<br>Lorem Ipsum has been the industry's<br>standard dummy text ever since the<br>1500s</p>
      <p>&nbsp;when an unknown printer took a<br>galley of type and scrambled it to<br>make a type specimen book. It has<br>survived not only five centuries.</p>
    </div>
  </section>

  <svg class="divider" width="580" height="14" viewBox="0 0 580 14" aria-hidden="true">
    <g fill="var(--dot-pink)">
      <circle cx="7" cy="7" r="6"/><circle cx="41.8" cy="7" r="6"/><circle cx="76.6" cy="7" r="6"/>
      <circle cx="111.4" cy="7" r="6"/><circle cx="146.2" cy="7" r="6"/><circle cx="181" cy="7" r="6"/>
      <circle cx="215.8" cy="7" r="6"/><circle cx="250.6" cy="7" r="6"/><circle cx="285.4" cy="7" r="6"/>
      <circle cx="320.2" cy="7" r="6"/><circle cx="355" cy="7" r="6"/><circle cx="389.8" cy="7" r="6"/>
      <circle cx="424.6" cy="7" r="6"/><circle cx="459.4" cy="7" r="6"/><circle cx="494.2" cy="7" r="6"/>
      <circle cx="529" cy="7" r="6"/><circle cx="563.8" cy="7" r="6"/>
    </g>
  </svg>

  <section class="step step--second">
    <div class="step__head">
      <span class="step__number">2</span>
      <h2 class="step__title">Title<br>Title Second Line</h2>
    </div>
    <div class="step__body">
      <p>Lorem Ipsum is simply dummy text of<br>the printing and typesetting industry.<br>Lorem Ipsum has been the industry's<br>standard dummy text ever since the<br>1500s</p>
      <p>&nbsp;when an unknown printer took a<br>galley of type and scrambled it to<br>make a type specimen book. It has<br>survived not only five centuries.</p>
    </div>
  </section>

  <div class="image-slot image-slot--second">IMAGE 1</div>

  <svg class="petal petal--upper" width="76" height="70" role="img" aria-label="Pink petal ornament">
    <rect width="76" height="70" rx="30" fill="var(--petal-pink)" opacity=".8"/>
  </svg>
  <svg class="petal petal--lower" width="76" height="70" role="img" aria-label="Pink petal ornament">
    <rect width="76" height="70" rx="30" fill="var(--petal-pink)" opacity=".8"/>
  </svg>
</body>
</html>
```